need a business card designed, I work with independent car dealerships throughout the US, I connect them with Buyers ( private investors, banks, credit unions, finance co's etc... ) that want to purchase their loan portfolio's, also consult on cashflow management, business lines of credit etc... looking for a consultant look, but something that attracts small business owners
Dunmore Consulting

```html
<!DOCTYPE html>
<html lang="en">
<head>
<meta charset="utf-8">
<title>Dunmore Consulting – Business Card</title>
<link href="https://fonts.googleapis.com/css2?family=Tauri&family=Source+Sans+3:wght@400&display=swap" rel="stylesheet">
<style>
  :root {
    --page-bg: #e9e9e9;
    --brand-red: #ec1c24;
    --name-red: #e3232a;
    --paper: #ffffff;
    --steel-top: #ffffff;
    --steel-bottom: #8f9094;
    --photo-dark: #1c242c;
    --photo-mid: #3b4852;
    --photo-light: #7f8c94;
    --contact-text: #ffffff;
  }
  * { margin: 0; padding: 0; box-sizing: border-box; }
  html, body {
    width: 1200px;
    height: 900px;
    overflow: hidden;
    background: var(--page-bg);
  }
  .canvas {
    position: relative;
    width: 1200px;
    height: 900px;
  }
  .business-card {
    position: absolute;
    left: 80px;
    top: 140px;
    width: 1040px;
    height: 620px;
    display: flex;
    box-shadow: 0 10px 30px rgba(0,0,0,0.18);
  }
  .card-left {
    position: relative;
    width: 585px;
    height: 100%;
    display: flex;
    flex-direction: column;
  }
  .steel-band {
    height: 170px;
    background: linear-gradient(to bottom, var(--steel-top) 0%, #d4d5d7 45%, var(--steel-bottom) 100%);
  }
  .name-band {
    height: 112px;
    background: var(--paper);
    display: flex;
    flex-direction: column;
    align-items: flex-end;
    justify-content: center;
    padding-right: 14px;
    font-family: "Tauri", sans-serif;
    color: var(--name-red);
    line-height: 1.05;
  }
  .person-name {
    font-size: 48px;
    letter-spacing: 0.5px;
  }
  .company-name {
    font-size: 36px;
    padding-right: 32px;
  }
  .dealership-photo {
    flex: 1;
    background:
      linear-gradient(160deg, rgba(180,60,60,0.35) 0%, rgba(180,60,60,0) 35%),
      linear-gradient(to bottom, var(--photo-light) 0%, var(--photo-mid) 30%, var(--photo-dark) 75%, #2b3238 100%);
  }
  .card-right {
    position: relative;
    flex: 1;
    background: var(--brand-red);
    color: var(--contact-text);
    font-family: "Source Sans 3", sans-serif;
  }
  .contact-list {
    position: absolute;
    left: 30px;
    bottom: 60px;
    display: grid;
    grid-template-columns: 80px 24px auto;
    row-gap: 14px;
    font-size: 28px;
    line-height: 1.2;
  }
</style>
</head>
<body>
<main class="canvas">
  <section class="business-card">
    <div class="card-left">
      <div class="steel-band"></div>
      <header class="name-band">
        <h1 class="person-name" style="font-weight:400">Daniel R Hollis</h1>
        <h2 class="company-name" style="font-weight:400">Dunmore Consulting</h2>
      </header>
      <div class="dealership-photo" role="img" aria-label="Photo of a row of parked cars on a dealership lot"></div>
    </div>
    <div class="card-right">
      <dl class="contact-list">
        <dt>Tel</dt><dd>:</dd><dd>303-555-0142</dd>
        <dt>Fax</dt><dd>:</dd><dd>303-555-0187</dd>
        <dt>E-mail</dt><dd>:</dd><dd>dealdesk7@mailbox.com</dd>
      </dl>
    </div>
  </section>
</main>
</body>
</html>
```